Quick Order Banner Design

We want to build a banner that will sit in the middle of the page that will replace our current quick order banner that we don't like. See https://www.snapglimmer.com/image/48273916?key=3f9b2c81d4e6a07f5c1b9e2d7a84f630

Text:
Quick Order is a fast and easy way to fill your cart with items when you know exactly what you want to purchase.

Design ideas:

Use foto Noto Sans. Color codes can be of #00539E, FDBC38, #6AC07A

We don't want a computer screen in banner nor a person. You can look at our competitors below for ideas.

i don't like the design here https://toblinmobilebits.com/blog/post/order-parts-fast-with-our-new-quick-order-feature but the concept is cool as it shows where to access it.. but i want other ideas too.

Our staging server is pelvant7.com

Our competitors:
https://www.quillonsupply.com/
https://www.brevolt.com/
https://www.zoska.com/
https://www.vimbo.com/index.html

Target Market(s)

B2B, Contractors who buy our products

Industry/Entity Type

hvac

Requirements
Should not have
• people photos or computer or computer screens.

```html
<!DOCTYPE html>
<html lang="en">
<head>
<meta charset="utf-8">
<title>Quick Order Banner</title>
<link href="https://fonts.googleapis.com/css2?family=Noto+Sans:wght@400;700&display=swap" rel="stylesheet">
<style>
  :root {
    --brand-blue: #00539E;
    --brand-yellow: #FDBC38;
    --brand-green: #6AC07A;
    --fold-black: #050505;
    --canvas: #FDFDFD;
    --preview-light: #ffffff;
    --preview-shade: #dfe1e4;
    --text-white: #ffffff;
  }
  * { box-sizing: border-box; margin: 0; padding: 0; }
  html, body { width: 1200px; height: 608px; overflow: hidden; }
  body { background: var(--canvas); font-family: "Noto Sans", sans-serif; position: relative; }

  .banner-shapes, .order-preview { position: absolute; left: 0; top: 0; }

  .banner-copy {
    position: absolute; left: 617px; top: 204px;
    font-size: 24.5px; line-height: 35px; color: var(--text-white); font-weight: 400;
    white-space: nowrap;
    transform: rotate(-0.6deg); transform-origin: left top;
  }
  .banner-copy__accent { color: var(--brand-yellow); font-weight: 700; }

  .quick-order-btn {
    position: absolute; left: 831px; top: 358px; width: 139px; height: 34px;
    background: var(--brand-yellow); color: var(--brand-blue);
    font-size: 12.5px; font-weight: 700; letter-spacing: 0.3px;
    display: flex; align-items: center; justify-content: center; text-decoration: none;
  }
</style>
</head>
<body>
  <svg class="banner-shapes" width="1200" height="608" viewBox="0 0 1200 608" aria-hidden="true">
    <rect x="221.5" y="172" width="758" height="265" fill="var(--brand-green)"/>
    <polygon points="184,207 221.5,186 221.5,207" fill="var(--fold-black)"/>
    <rect x="184" y="207" width="37.5" height="223" fill="var(--brand-blue)"/>
    <polygon points="979.5,403 1016,401 979.5,421" fill="var(--fold-black)"/>
    <polygon points="578,194 1016,180 1016,401 578,417" fill="var(--brand-blue)"/>
  </svg>

  <svg class="order-preview" width="1200" height="608" viewBox="0 0 1200 608" role="img"
       aria-label="Screenshot of the Quick Order page showing product rows with quantities and prices, and a CSV import and paste order panel">
    <defs>
      <linearGradient id="preview-tone" x1="0" y1="0" x2="1" y2="0">
        <stop offset="0" stop-color="var(--preview-light)"/>
        <stop offset="0.7" stop-color="var(--preview-light)"/>
        <stop offset="1" stop-color="var(--preview-shade)"/>
      </linearGradient>
    </defs>
    <polygon points="213,204 580,194 584,417 217,430" fill="url(#preview-tone)"/>
  </svg>

  <p class="banner-copy">
    <span class="banner-copy__accent">Quick Order</span> is a fast and easy<br>
    way to <span class="banner-copy__accent">fill your cart</span> with items<br>
    when you know exactly<br>
    what you want <span class="banner-copy__accent">to purchase.</span>
  </p>
  <a class="quick-order-btn" href="#">QUICK ORDER</a>
</body>
</html>
```